Residential Roofing Company, need a Unique business card for a Woman owned ompany

Woman Owned Residential Roofing Company. Specializing in Insurance Claims
Attention to Detail is what sets this woman owned roofing company apart from the rest
We are TRV Certified and are an Accredited business with an A rating with the QPL. Our Contractor License number KMT48395

```html
<!DOCTYPE html>
<html lang="en">
<head>
<meta charset="utf-8">
<title>Ridgeway Roofing – Business Card</title>
<link rel="stylesheet" href="https://fonts.googleapis.com/css2?family=Open+Sans:wght@400;600;800&display=swap">
<style>
  :root{
    --stage:#3b3c3f;
    --navy:#243463;
    --navy-faint:#34447a;
    --ink:#111217;
    --white:#ffffff;
    --badge-blue:#1b6c9c;
  }
  *{box-sizing:border-box;margin:0;padding:0}
  html,body{width:1200px;height:801px;overflow:hidden}
  body{background:var(--stage);font-family:"Open Sans",Arial,sans-serif;position:relative}
  .card{position:absolute;top:246px;width:540px;height:308px;border-radius:22px;overflow:hidden}
  .card--back{left:40px;background:var(--navy)}
  .card--front{left:620px;background:var(--white)}
  .back-mark{position:absolute;inset:0;display:flex;align-items:center;justify-content:center;gap:10px}
  .back-mark__square{width:14px;height:14px;background:var(--navy-faint)}
  .back-mark__name{font-weight:800;font-size:34px;color:var(--navy-faint);letter-spacing:.5px}
  .wave{position:absolute;inset:0;width:100%;height:100%}
  .badge{position:absolute;left:28px;top:34px;width:156px;height:58px}
  .brand{position:absolute;right:30px;top:28px;text-align:right}
  .brand__row{display:flex;align-items:center;justify-content:flex-end;gap:8px}
  .brand__square{width:12px;height:12px;background:var(--navy)}
  .brand__name{font-weight:800;font-size:22px;color:var(--navy);letter-spacing:.3px}
  .brand__license{font-size:10.5px;color:var(--ink);margin-top:4px}
  .person{position:absolute;left:30px;top:172px;color:var(--white)}
  .person__name{font-weight:600;font-size:22px;line-height:1.1}
  .person__title{font-size:12px;margin-top:3px;padding-bottom:6px;border-bottom:1px solid var(--white);width:190px}
  .contacts{list-style:none;margin-top:7px}
  .contacts li{display:flex;align-items:center;gap:8px;font-size:11.5px;line-height:17px}
  .contacts svg{width:11px;height:11px;fill:var(--white);flex:none}
  .address{position:absolute;right:30px;top:200px;color:var(--white);font-size:11.5px;line-height:17px;text-align:right;font-style:normal}
</style>
</head>
<body>
  <section class="card card--back" aria-label="Card back">
    <div class="back-mark">
      <span class="back-mark__square"></span>
      <span class="back-mark__name">RIDGEWAY ROOFING</span>
    </div>
  </section>

  <section class="card card--front" aria-label="Card front">
    <svg class="wave" viewBox="0 0 540 308" preserveAspectRatio="none">
      <path d="M0,150 C160,108 330,122 540,96 L540,308 L0,308Z" fill="var(--ink)"/>
      <path d="M0,164 C165,122 335,136 540,110 L540,308 L0,308Z" fill="var(--navy)"/>
    </svg>

    <svg class="badge" viewBox="0 0 156 58" role="img" aria-label="Accreditation badge">
      <rect x="1" y="1" width="154" height="56" rx="6" fill="var(--white)" stroke="var(--badge-blue)" stroke-width="2"/>
      <rect x="50" y="1" width="105" height="56" rx="6" fill="var(--badge-blue)"/>
      <rect x="50" y="1" width="10" height="56" fill="var(--badge-blue)"/>
    </svg>

    <div class="brand">
      <div class="brand__row">
        <span class="brand__square"></span>
        <span class="brand__name">RIDGEWAY ROOFING</span>
      </div>
      <div class="brand__license">Contractor License number KMT48395</div>
    </div>

    <div class="person">
      <div class="person__name">Nora Halvorsen</div>
      <div class="person__title">Chief Executive Officer</div>
      <ul class="contacts">
        <li><svg viewBox="0 0 24 24"><path d="M6.6 10.8a15.1 15.1 0 0 0 6.6 6.6l2.2-2.2c.3-.3.7-.4 1-.2 1.1.4 2.3.6 3.6.6.6 0 1 .4 1 1V20c0 .6-.4 1-1 1A17 17 0 0 1 3 4c0-.6.4-1 1-1h3.5c.6 0 1 .4 1 1 0 1.3.2 2.5.6 3.6.1.3 0 .7-.2 1z"/></svg>555.210.4481</li>
        <li><svg viewBox="0 0 24 24"><path d="M7 1h10a2 2 0 0 1 2 2v18a2 2 0 0 1-2 2H7a2 2 0 0 1-2-2V3a2 2 0 0 1 2-2zm0 3v14h10V4z"/></svg>555.210.4492</li>
        <li><svg viewBox="0 0 24 24"><path d="M2 5h20v14H2zm2 2v.5l8 5 8-5V7z"/></svg>nora@ridgewayroofs.com</li>
        <li><svg viewBox="0 0 24 24"><circle cx="12" cy="12" r="10"/></svg>www.ridgewayroofs.com</li>
      </ul>
    </div>

    <address class="address">48 Alder Lane<br>Westbrook MA 02190</address>
  </section>
</body>
</html>
```